Design a Full Page PDF Brochure "white paper" (Adobe InDesign)

Hello, my business needs a template to create "white papers" for our website. These are the free PDF downloads that you see on websites for lead capture.

The winning entry will need the following seven characteristics:
(1) A consistent color palette (or scheme) and feel of our website and logo (which I've attached). Even thought it is called a "white paper", please use lots of color and make it vibrant.
(2) A cover sheet that fills up the whole page, it also needs to have contact information on it (you can use this for now):

Derek Falmouth
48 Orchard Ln
Springfield, USA
888-414-2626
derek@[login to view URL]

It's important that our logo is used as part of the cover page design. Feel free to be creative with this.

(3) The text needs to have different sized subheadings (H1, H2, H3)
(4) I would suggest adding "call outs" to highlight quotes from the text
(5) I would suggest submitting entries with multiple page layouts that can be used
(6) You may use Latin text and stock photos that I will replace. Our website [login to view URL] uses a theme of hiking, mountains, and paths.
(7) The final page needs to also have the contact information on it

To help clarify what I'm looking for, here are some examples of white papers:

The entries need to be in Adobe InDesign. The winner needs to turn over the final InDesign Files along with any supporting files such as in Adobe Illustrator.

Also, please do not contact me outside of Taskwharf (doing so will disqualify your entries).

Thank you ahead of time for your work.

```html
<!DOCTYPE html>
<html lang="en">
<head>
<meta charset="utf-8">
<title>Trailmark Advisors – White Paper Cover Spread</title>
<link href="https://fonts.googleapis.com/css2?family=Roboto:wght@300;400;700&family=Roboto+Condensed:wght@300;700&display=swap" rel="stylesheet">
<style>
  :root {
    --backdrop: #e4e4e4;
    --leaf: #8cb83c;
    --leaf-deep: #7aa532;
    --paper: #f4f5f9;
    --ink-light: #ffffff;
    --ink-muted: #6f7a5a;
    --rock: #9c9c94;
    --rock-dark: #5d605a;
    --ridge: #4d5552;
    --sky: #c9d0d6;
    --moss: #4f6a3a;
  }
  * { box-sizing: border-box; margin: 0; padding: 0; }
  html, body {
    width: 1200px; height: 788px; overflow: hidden;
    background: var(--backdrop);
    font-family: "Roboto", Arial, sans-serif;
  }
  .spread {
    position: absolute; left: 100px; top: 71px;
    width: 1000px; height: 646px;
    display: flex;
    box-shadow: 0 10px 30px rgba(0,0,0,.18);
  }
  .page { position: relative; width: 500px; height: 646px; overflow: hidden; }

  /* Back cover */
  .back-photo {
    position: absolute; left: 0; top: 0; width: 150px; height: 100%;
    background: linear-gradient(180deg, var(--ridge) 0%, var(--moss) 22%, var(--rock) 45%, var(--rock-dark) 75%, var(--rock) 100%);
  }
  .back-panel {
    position: absolute; left: 150px; top: 0; right: 0; height: 100%;
    background: var(--leaf);
  }
  .contacts {
    position: absolute; left: 22px; top: 300px;
    color: var(--ink-light);
  }
  .brand {
    display: flex; align-items: center; gap: 6px;
    font-size: 10px; font-weight: 700; letter-spacing: .5px;
    text-transform: uppercase; margin-bottom: 14px;
  }
  .brand-dot { width: 10px; height: 10px; border-radius: 50%; background: currentColor; }
  .contact { margin-bottom: 12px; font-size: 9px; line-height: 1.35; }
  .contact-name { font-weight: 700; text-transform: uppercase; letter-spacing: .4px; }

  /* Front cover */
  .front-photo {
    position: absolute; left: 0; top: 0; width: 330px; height: 100%;
    background: linear-gradient(180deg, var(--sky) 0%, var(--ridge) 18%, var(--moss) 38%, var(--rock) 55%, var(--rock-dark) 80%, var(--rock) 100%);
  }
  .front-column {
    position: absolute; left: 330px; top: 0; right: 0; height: 100%;
    background: var(--paper);
  }
  .front-stripe {
    position: absolute; left: 330px; top: 0; width: 10px; height: 215px;
    background: var(--leaf);
  }
  .front-brand {
    position: absolute; left: 340px; right: 0; top: 30px;
    display: flex; justify-content: center; align-items: center; gap: 6px;
    color: var(--leaf-deep); font-size: 11px; font-weight: 700;
    letter-spacing: .5px; text-transform: uppercase;
  }
  .headline-box {
    position: absolute; left: 268px; top: 262px; width: 232px; height: 175px;
    background: var(--leaf); color: var(--ink-light);
    padding: 22px 20px;
  }
  .headline {
    font-family: "Roboto Condensed", Arial, sans-serif;
    text-transform: uppercase; line-height: 1;
  }
  .headline-lead { display: block; font-weight: 300; font-size: 21px; }
  .headline-main { display: block; font-weight: 700; font-size: 29px; margin-top: 2px; }
  .headline-body { margin-top: 10px; font-size: 7.5px; line-height: 1.4; font-weight: 400; }
  .web {
    position: absolute; right: 22px; bottom: 30px;
    font-size: 8px; color: var(--ink-muted);
  }
</style>
</head>
<body>
  <main class="spread">
    <section class="page page-back">
      <div class="back-photo" role="img" aria-label="Stock photo of a rocky mountain trail with shrubs"></div>
      <div class="back-panel">
        <div class="contacts">
          <div class="brand"><span class="brand-dot"></span>Trailmark Advisors</div>
          <div class="contact">
            <div class="contact-name">Derek Falmouth</div>
            <div>555.414.2626</div>
            <div>derek@trailmarkadvisors.com</div>
          </div>
          <div class="contact">
            <div class="contact-name">Lena Okafor</div>
            <div>555.203.7741</div>
            <div>lena@trailmarkadvisors.com</div>
          </div>
          <div class="contact">
            <div class="contact-name">Theo Brandt</div>
            <div>555.318.4460</div>
            <div>theo@trailmarkadvisors.com</div>
          </div>
          <div class="contact">
            <div class="contact-name">Rosa Whitcombe</div>
            <div>rosa@trailmarkadvisors.com</div>
          </div>
        </div>
      </div>
    </section>

    <section class="page page-front">
      <div class="front-photo" role="img" aria-label="Stock photo of a hiker with a backpack on a rocky path facing mountain peaks"></div>
      <div class="front-column"></div>
      <div class="front-stripe"></div>
      <div class="front-brand"><span class="brand-dot"></span>Trailmark Advisors</div>
      <div class="headline-box">
        <h1 class="headline">
          <span class="headline-lead">We make</span>
          <span class="headline-main">The complex<br>simple</span>
        </h1>
        <p class="headline-body">Most people share a central fear: that at some point in their lives, they will need money and not have it. Wealth is the absence of that fear.</p>
      </div>
      <div class="web">www.trailmarkadvisors.com</div>
    </section>
  </main>
</body>
</html>
```